Business card for exciting VC company

Should look simple, crisp, and modern.

Industry/Entity Type

Venture Capital

Contact Information for Business Card

Would like to see at least one design that has our blue on the back with the tagline "Transforming Traditional Industry" and white front with contact details.

Font styles to use
Sans Serif

Requirements
Must have
• Logo

Gregory Tallis
gtallis@brindlewave.vc
Managing Partner
M (628)354-xxxx

```html
<!DOCTYPE html>
<html lang="en">
<head>
<meta charset="utf-8">
<title>Brindlewave Capital — Business Card</title>
<link rel="stylesheet" href="https://fonts.googleapis.com/css2?family=Montserrat:wght@500;700&family=Lato:wght@400&display=swap">
<style>
  :root {
    --brand-blue: #4384c4;
    --brand-blue-light: #7db2de;
    --ink: #1c1c1c;
    --ink-muted: #6b6b6b;
    --paper: #ffffff;
    --backdrop: #ececee;
  }
  * { margin: 0; padding: 0; box-sizing: border-box; }
  html, body {
    width: 1200px; height: 1200px; overflow: hidden;
    background: var(--backdrop);
  }
  .sheet { position: relative; width: 1200px; height: 1200px; }

  .card {
    position: absolute; left: 246px; width: 762px; height: 436px;
    box-shadow: 0 6px 14px rgba(0,0,0,0.22);
    overflow: hidden;
  }

  /* Brand side */
  .card--brand {
    top: 175px;
    background:
      radial-gradient(ellipse 340px 260px at 560px 40px, var(--brand-blue-light), transparent 75%),
      var(--brand-blue);
  }
  .brand-wordmark {
    position: absolute; left: 0; right: 0; top: 180px;
    text-align: center;
    font-family: "Montserrat", sans-serif; font-weight: 500;
    font-size: 34px; letter-spacing: 0.12em;
    color: var(--paper);
  }
  .tagline-band {
    position: absolute; left: 0; right: 0; top: 354px; height: 41px;
    background: var(--paper);
    box-shadow: 0 2px 4px rgba(0,0,0,0.25);
    display: flex; align-items: center; justify-content: center;
  }
  .tagline {
    font-family: "Lato", sans-serif; font-weight: 400;
    font-size: 20px; color: var(--brand-blue);
  }

  /* Contact side */
  .card--contact { top: 643px; background: var(--paper); }
  .person {
    position: absolute; left: 35px; top: 140px;
  }
  .person__name {
    font-family: "Montserrat", sans-serif; font-weight: 700;
    font-size: 29px; letter-spacing: 0.03em; color: var(--ink);
    line-height: 1.1;
  }
  .person__role {
    margin-top: 6px;
    font-family: "Lato", sans-serif; font-size: 16px; letter-spacing: 0.04em;
    color: var(--ink-muted);
  }
  .contact-list { list-style: none; margin-top: 22px; }
  .contact-list__item {
    display: flex; align-items: center; gap: 10px; height: 27px;
    font-family: "Lato", sans-serif; font-size: 17px; letter-spacing: 0.03em;
    color: var(--ink-muted);
  }
  .contact-list__icon { width: 25px; height: 25px; flex: none; }

  .contact-wordmark {
    position: absolute; left: 420px; right: 20px; top: 208px;
    text-align: center;
    font-family: "Montserrat", sans-serif; font-weight: 500;
    font-size: 22px; letter-spacing: 0.1em;
    color: var(--ink);
  }
</style>
</head>
<body>
<main class="sheet">
  <section class="card card--brand">
    <div class="brand-wordmark">BRINDLEWAVE CAPITAL</div>
    <div class="tagline-band">
      <p class="tagline">-TRANSFORMING TRADITIONAL INDUSTRY-</p>
    </div>
  </section>

  <section class="card card--contact">
    <div class="person">
      <h1 class="person__name">GREGORY TALLIS</h1>
      <p class="person__role">MANAGING PARTNER</p>
      <ul class="contact-list">
        <li class="contact-list__item">
          <svg class="contact-list__icon" viewBox="0 0 26 26" aria-hidden="true">
            <circle cx="13" cy="13" r="11.5" fill="none" stroke="var(--brand-blue)" stroke-width="1.6"/>
            <path d="M9.2 7.8c.6-.5 1.3-.4 1.6.2l.9 1.8c.2.5.1 1-.3 1.3l-.6.5c.6 1.4 1.6 2.5 3 3.1l.5-.6c.3-.4.9-.5 1.3-.3l1.8.9c.6.3.7 1 .2 1.6-.9 1-2.2 1.3-3.5.7-2.6-1.2-4.5-3.2-5.6-5.8-.5-1.2-.2-2.6.7-3.4z" fill="var(--brand-blue)"/>
          </svg>
          <span>(628)354-xxxx</span>
        </li>
        <li class="contact-list__item">
          <svg class="contact-list__icon" viewBox="0 0 26 26" aria-hidden="true">
            <circle cx="13" cy="13" r="11.5" fill="none" stroke="var(--brand-blue)" stroke-width="1.6"/>
            <rect x="7.5" y="9.5" width="11" height="7.5" rx="0.8" fill="var(--brand-blue)"/>
            <path d="M7.8 10l5.2 4 5.2-4" fill="none" stroke="#fff" stroke-width="1"/>
          </svg>
          <span>gtallis@brindlewave.vc</span>
        </li>
        <li class="contact-list__item">
          <svg class="contact-list__icon" viewBox="0 0 26 26" aria-hidden="true">
            <circle cx="13" cy="13" r="11.5" fill="none" stroke="var(--brand-blue)" stroke-width="1.6"/>
            <path d="M10.5 7.5v10l2.4-2.3 1.6 3.3 1.4-.7-1.6-3.2h3.2z" fill="var(--brand-blue)"/>
          </svg>
          <span>www.brindlewave.com</span>
        </li>
      </ul>
    </div>
    <div class="contact-wordmark">BRINDLEWAVE CAPITAL</div>
  </section>
</main>
</body>
</html>
```